Organic Soap Packaging

We need a package design for a new company called Fern Naturals. Our primary product is organic soap. Our business model is based on the social entrepreneurial concept of by one give one like Valo shoes. We are giving soap to help prevent the spread of disease; 1.4 million deaths a year can be prevented by hand washing.

The design is for a recycled cardboard box/package. We want to demonstrate the high end, luxury feel of the product with undertones of organic/earth friendly/social conscious.

The soap is small batch, spa like, essential oil scented all natural luxury.
Updates

I am very excited about this startup business and I believe we will have great success! I am passionate about organic personal care and helping others in need. If you share my passion, please bring your work to the table!

Target Market(s)

My target market is people who are educated through college. Health conscious, socially conscious, Generation X. Basically shoppers of Green Basket and Halvorsen.

Industry/Entity Type

Business

Requirements
Must have
• Suitable for Face, Hair, and Skin
Scented with Organic Essential Oils

```html
<!DOCTYPE html>
<html lang="en">
<head>
<meta charset="utf-8">
<title>Fern Naturals – Organic Soap Packaging</title>
<link rel="stylesheet" href="https://fonts.googleapis.com/css2?family=Handlee&family=Crimson+Text&display=swap">
<style>
  :root {
    --forest: #42622a;
    --olive: #98a03e;
    --paper: #ffffff;
    --glow: rgba(150, 160, 90, 0.45);
    --ink: #42622a;
    --floor: #000000;
  }
  html, body {
    margin: 0;
    padding: 0;
    width: 1200px;
    height: 1000px;
    overflow: hidden;
    background: var(--paper);
  }
  .sheet { display: block; width: 1200px; height: 1000px; }
  .front-panel, .dieline { filter: drop-shadow(0 0 18px var(--glow)); }
  .forest { fill: var(--forest); }
  .olive { fill: var(--olive); }
  .band { fill: var(--paper); }
  .flap { fill: var(--paper); stroke: var(--ink); stroke-width: 1; }
  .brand-name { font-family: "Handlee", cursive; fill: var(--forest); }
  .script { font-family: "Handlee", cursive; fill: var(--paper); text-anchor: middle; }
  .serif { font-family: "Crimson Text", serif; fill: var(--paper); text-anchor: middle; }
  .flap-label { font-family: Arial, Helvetica, sans-serif; font-size: 11px; fill: var(--ink); text-anchor: middle; }
  .wreath { fill: none; stroke: var(--paper); stroke-width: 3; opacity: 0.85; }
  .floor { fill: var(--floor); }
</style>
</head>
<body>
<svg class="sheet" viewBox="0 0 1200 1000" xmlns="http://www.w3.org/2000/svg">

  <!-- Front panel -->
  <g class="front-panel">
    <rect class="forest" x="135" y="99" width="242" height="376"/>
    <rect class="band" x="135" y="124" width="242" height="37"/>
    <rect class="band" x="163" y="161" width="38" height="314"/>
    <text class="brand-name" x="182" y="148" font-size="16" text-anchor="middle">Fern Naturals</text>

    <text class="script" x="289" y="218" font-size="19">Luxury</text>
    <text class="script" x="289" y="242" font-size="17">Organic</text>
    <text class="script" x="289" y="264" font-size="17">Soap</text>
    <text class="script" x="289" y="284" font-size="15">scented</text>
    <text class="script" x="289" y="302" font-size="14">with</text>
    <text class="script" x="289" y="318" font-size="12">Essential</text>
    <text class="script" x="289" y="332" font-size="11">Oils.</text>

    <g role="img" aria-label="Leaf wreath emblem">
      <circle class="wreath" cx="285" cy="384" r="20"/>
    </g>

    <text class="serif" x="289" y="442" font-size="11">This product is suitable</text>
    <text class="serif" x="289" y="456" font-size="11">for Face, Hair and Body.</text>
  </g>

  <!-- Box dieline -->
  <g class="dieline">
    <polygon class="flap" points="684,357 828,357 840,405 672,405"/>
    <polygon class="flap" points="672,857 840,857 828,905 684,905"/>
    <polygon class="flap" points="1004,857 1050,857 1044,905 1010,905"/>
    <polygon class="flap" points="1105,500 1155,515 1155,745 1105,760"/>

    <polygon class="olive" points="620,415 893,415 935,452 935,810 893,847 620,847 577,810 577,452"/>
    <rect class="olive" x="935" y="500" width="170" height="357"/>

    <rect class="forest" x="671" y="498" width="169" height="264"/>
    <rect class="forest" x="935" y="500" width="170" height="262"/>
    <ellipse class="band" cx="1018" cy="500" rx="30" ry="15"/>

    <rect class="band" x="688" y="357" width="26" height="500"/>
    <rect class="band" x="577" y="515" width="528" height="26"/>
    <text class="brand-name" x="701" y="532" font-size="11" text-anchor="middle">Fern Naturals</text>

    <text class="script" x="771" y="577" font-size="13">Luxury</text>
    <text class="script" x="771" y="592" font-size="12">Organic</text>
    <text class="script" x="771" y="607" font-size="12">Soap</text>
    <text class="script" x="771" y="621" font-size="10">scented</text>
    <text class="script" x="771" y="633" font-size="9">with</text>
    <text class="script" x="771" y="644" font-size="8">Essential</text>
    <text class="script" x="771" y="654" font-size="7">Oils.</text>

    <g role="img" aria-label="Leaf wreath emblem">
      <circle class="wreath" cx="769" cy="685" r="13" stroke-width="2"/>
    </g>

    <text class="serif" x="773" y="730" font-size="8">This product is suitable</text>
    <text class="serif" x="773" y="739" font-size="8">for Face, Hair and Body.</text>

    <text class="serif" x="1020" y="580" font-size="11">Buy 1</text>
    <text class="serif" x="1020" y="594" font-size="11">Give 1</text>
    <text class="serif" x="1020" y="607" font-size="11">and</text>
    <text class="serif" x="1020" y="620" font-size="11">help</text>
    <text class="serif" x="1020" y="633" font-size="11">us</text>
    <text class="serif" x="1020" y="646" font-size="11">prevent</text>
    <text class="serif" x="1020" y="659" font-size="11">the</text>
    <text class="serif" x="1020" y="672" font-size="11">spread</text>
    <text class="serif" x="1020" y="685" font-size="11">of</text>
    <text class="serif" x="1020" y="698" font-size="11">disease;</text>
    <text class="serif" x="1020" y="732" font-size="10">1.4 million deaths a year</text>
    <text class="serif" x="1020" y="746" font-size="10">can be prevented by hand washing.</text>

    <text class="flap-label" x="749" y="387">top</text>
    <text class="flap-label" x="756" y="884">bottom</text>
    <text class="flap-label" x="1128" y="633">glue</text>
  </g>

  <rect class="floor" x="0" y="958" width="1200" height="42"/>
</svg>
</body>
</html>
```